Business card

We are looking for a creative person to deigns our company business card.

Target Market(s)

College age student

Industry/Entity Type

Accommodation

Contact Information for Business Card

We want a fun, clean and sophisticated design. It should look good, but more importantly the information should be legible.

Font styles to use
Serif
Sans Serif
Other font styles liked:
• Open Sans ,

Colors
33a6d7

Requirements
Must have
• Must have a young and memorable message. Be legible.
• Our logo on the back on a solid blue , please find color and logo attached
• LodgeNestly.com on the back.
Nice to have
• I would like to have couple of different fonts on the LodgeNestly.com on the back of the cards with a solid blue.

```html
<!DOCTYPE html>
<html lang="en">
<head>
<meta charset="utf-8">
<title>LodgeNestly Business Card</title>
<link rel="stylesheet" href="https://fonts.googleapis.com/css2?family=Roboto:wght@400;700&family=Roboto+Condensed:wght@700&display=swap">
<style>
  :root {
    --page-bg: #2a2a2a;
    --brand-navy: #03507f;
    --brand-dark: #0a4f7c;
    --brand-light: #3a9ad9;
    --card-white: #f1f1f1;
    --text-grey: #4a4a4a;
    --front-text: #ffffff;
  }
  html, body {
    margin: 0;
    padding: 0;
    width: 1200px;
    height: 960px;
    overflow: hidden;
    background: var(--page-bg);
  }
  .canvas {
    position: relative;
    width: 1200px;
    height: 960px;
  }
  .card {
    position: absolute;
    left: 320px;
    width: 600px;
    height: 342px;
    box-sizing: border-box;
  }
  .card-front {
    top: 108px;
    background: var(--brand-navy);
    display: flex;
    align-items: center;
    justify-content: center;
  }
  .front-wordmark {
    font-family: "Roboto", Arial, sans-serif;
    font-weight: 700;
    font-size: 44px;
    letter-spacing: -1px;
    color: var(--front-text);
  }
  .card-back {
    top: 493px;
    background: var(--card-white);
    padding: 30px 32px;
    font-family: "Roboto", Arial, sans-serif;
    color: var(--text-grey);
  }
  .back-wordmark {
    font-weight: 700;
    font-size: 29px;
    letter-spacing: -0.6px;
    color: var(--brand-dark);
    line-height: 1;
    margin: 0;
  }
  .person-name {
    font-family: "Roboto Condensed", Arial, sans-serif;
    font-weight: 700;
    font-size: 21px;
    color: var(--brand-dark);
    margin: 58px 0 0;
    line-height: 1;
  }
  .person-title {
    font-size: 15px;
    color: var(--brand-light);
    margin: 6px 0 0;
    line-height: 1;
  }
  .address {
    font-size: 14.5px;
    line-height: 18.5px;
    margin: 14px 0 0;
    font-style: normal;
  }
  .contact-list {
    list-style: none;
    padding: 0;
    margin: 10px 0 0;
    font-size: 14.5px;
    line-height: 19px;
  }
  .contact-list li {
    display: flex;
    align-items: center;
    gap: 9px;
  }
  .contact-icon {
    width: 14px;
    height: 14px;
    fill: var(--brand-dark);
    flex: none;
  }
</style>
</head>
<body>
<main class="canvas">
  <section class="card card-front" aria-label="Card front">
    <span class="front-wordmark">LodgeNestly</span>
  </section>

  <section class="card card-back" aria-label="Card back">
    <p class="back-wordmark">LodgeNestly</p>
    <h1 class="person-name">DANIEL REYES</h1>
    <p class="person-title">CEO/FOUNDER</p>
    <address class="address">118 Marlow Ave., Suite 302.<br>Fairview<br>California CA 90187</address>
    <ul class="contact-list">
      <li><svg class="contact-icon" viewBox="0 0 14 14" aria-hidden="true"><path d="M3 1l2.5 3-1.4 1.6c.8 1.7 2 2.9 3.7 3.7L9.4 8 12.5 10.5 11 13C6 12.6 1.4 8 1 3z"/></svg>555 210 4871</li>
      <li><svg class="contact-icon" viewBox="0 0 14 14" aria-hidden="true"><path d="M4 0h6a1 1 0 0 1 1 1v12a1 1 0 0 1-1 1H4a1 1 0 0 1-1-1V1a1 1 0 0 1 1-1zm.5 1.5v9h5v-9zM7 11.4a.8.8 0 1 0 0 1.6.8.8 0 0 0 0-1.6z"/></svg>555 392 6604</li>
      <li><svg class="contact-icon" viewBox="0 0 14 14" aria-hidden="true"><path d="M3 1h8v3H3zM1 5h12v6h-2V9H3v2H1zM3.5 10h7v3h-7z"/></svg>555 718 2253</li>
      <li><svg class="contact-icon" viewBox="0 0 14 14" aria-hidden="true"><path d="M1 3h12v1.2L7 8 1 4.2zM1 5.6l6 3.8 6-3.8V11H1z"/></svg>daniel@LodgeNestly.com</li>
      <li><svg class="contact-icon" viewBox="0 0 14 14" aria-hidden="true"><path d="M7 1a6 6 0 1 0 0 12A6 6 0 0 0 7 1zm0 1.4c.9 0 1.7 2 1.9 4H5.1C5.3 4.4 6.1 2.4 7 2.4zM5.1 7.6h3.8c-.2 2-1 4-1.9 4s-1.7-2-1.9-4z"/></svg>www.LodgeNestly.com</li>
    </ul>
  </section>
</main>
</body>
</html>
```